label design for oral care product

Kindly invite you to design bottle label (114 mm*40 mm) for our product, a kind of oral care product. The GEL is different from our previous cleanser product, as the pic we uploaded for demonstration. The color of frosted glass bottle is dark green, but the cap is white. You could download the pic of bottle among the uploaded files. The logo file and label content description are attached too. Please check them. Our product is made from many kinds of natural plant extracts, which includes herb and fruit. I wish the label would make our product look high-end and reliable. And it would be better if you could give some advice on paper material and special requirements for printing, related to your design. I value the texture of label too, because I think that stands for the quality of products. No color limitation for the use of our logo.
Target Market(s)
20-40 female, who value oral health.
Colors
Designer to choose colors to be used in the design.
Look and feel
Each slider illustrates characteristics of the customer's brand and the style your logo design should communicate.

```html
<!DOCTYPE html>
<html lang="en">
<head>
<meta charset="utf-8">
<title>Aligner Gel – Label Presentation</title>
<link rel="stylesheet" href="https://fonts.googleapis.com/css2?family=Marcellus&family=Open+Sans:wght@400;600;700&family=Alegreya+Sans:ital,wght@1,400;1,500&display=swap">
<style>
  :root {
    --page: #0a0b17;
    --olive: #3e4120;
    --olive-deep: #35381b;
    --olive-edge: #464a27;
    --ink: #ffffff;
    --ink-soft: #e4e4dc;
    --cap: #e9e9e6;
  }
  * { margin: 0; padding: 0; box-sizing: border-box; }
  html, body { width: 960px; height: 1200px; overflow: hidden; background: var(--page); }
  .board { position: relative; width: 960px; height: 1200px; color: var(--ink); font-family: "Open Sans", sans-serif; }

  .abs { position: absolute; text-align: center; white-space: nowrap; }

  .wordmark { position: absolute; display: flex; align-items: center; justify-content: center; gap: 6px;
    font-family: "Open Sans", sans-serif; font-weight: 700; color: var(--ink); letter-spacing: 0.5px; }
  .wordmark .dot { border-radius: 50%; background: var(--ink); display: inline-block; }

  .title-serif { font-family: "Marcellus", serif; letter-spacing: 0.5px; }
  .caps { letter-spacing: 2px; text-transform: uppercase; }
  .tagline { font-family: "Alegreya Sans", sans-serif; font-style: italic; }

  /* bottle showcase */
  .bottle-shot { position: absolute; left: 178px; top: 130px; width: 246px; height: 632px;
    border-radius: 40px 40px 16px 16px;
    background: linear-gradient(180deg, var(--cap) 0%, var(--cap) 24%, #5a5f2c 34%, #3f4320 70%, #2f3218 100%); }
  .bottle-label { position: absolute; left: 178px; top: 130px; width: 246px; height: 632px; }

  /* front label */
  .front-label { position: absolute; left: 491px; top: 130px; width: 289px; height: 642px; background: var(--olive); }

  /* wrap label */
  .wrap-label { position: absolute; left: 118px; top: 826px; width: 733px; height: 257px; background: var(--olive-edge); overflow: hidden; }
  .band { position: absolute; top: 0; height: 100%; background: var(--olive-deep); }
  .band.back { left: 54px; width: 324px; }
  .band.spine { left: 378px; width: 68px; background: var(--olive); }
  .band.face { left: 446px; width: 236px; }

  .section-head { position: absolute; left: 104px; font-weight: 700; font-size: 15.5px; letter-spacing: 1.6px; white-space: nowrap; }
  .section-head::before { content: ""; position: absolute; left: -20px; top: 7px; width: 8px; height: 8px; background: var(--ink); }
  .body-copy { position: absolute; left: 102px; font-size: 13.4px; line-height: 18px; color: var(--ink-soft); white-space: nowrap; }

  .spine-text { position: absolute; left: 412px; top: 130px; transform: translate(-50%, -50%) rotate(-90deg);
    font-weight: 700; font-size: 12.5px; letter-spacing: 1.6px; white-space: nowrap; }
</style>
</head>
<body>
<main class="board">

  <!-- bottle showcase -->
  <div class="bottle-shot" role="img" aria-label="Product shot of the dark green frosted glass dropper bottle with white cap"></div>
  <div class="bottle-label">
    <div class="wordmark" style="left:0;width:246px;top:346px;font-size:27px;">Lumi Leaf<span class="dot" style="width:9px;height:9px;"></span></div>
    <div class="abs title-serif" style="left:0;width:246px;top:424px;font-size:27px;">ALIGNER GEL</div>
    <div class="abs caps" style="left:0;width:246px;top:465px;font-size:14px;line-height:19px;">Immune support for<br>oral health</div>
    <div class="abs tagline" style="left:0;width:246px;top:518px;font-size:12.5px;line-height:15.5px;">The Solution to Maintain Dental<br>Hygiene and Strengthen Gums</div>
    <div class="abs tagline" style="left:0;width:246px;top:562px;font-size:12.5px;">Made in Taiwan</div>
  </div>

  <!-- front label -->
  <section class="front-label">
    <div class="wordmark" style="left:0;width:289px;top:112px;font-size:34px;">Lumi Leaf<span class="dot" style="width:11px;height:11px;"></span></div>
    <div class="abs title-serif" style="left:0;width:289px;top:258px;font-size:32px;">ALIGNER GEL</div>
    <div class="abs caps" style="left:0;width:289px;top:300px;font-size:18.5px;line-height:27px;">Immune support for<br>oral health</div>
    <div class="abs tagline" style="left:0;width:289px;top:414px;font-size:18px;line-height:23px;">The Solution to Maintain Dental<br>Hygiene and Strengthen Gums</div>
    <div class="abs title-serif" style="left:0;width:289px;top:518px;font-size:21px;letter-spacing:1.5px;">30 ML</div>
    <div class="abs tagline" style="left:0;width:289px;top:581px;font-size:18px;">Made in Taiwan</div>
  </section>

  <!-- wrap-around label -->
  <section class="wrap-label">
    <div class="band back"></div>
    <div class="band spine"></div>
    <div class="band face"></div>

    <div class="section-head" style="top:15px;">PRODUCT CONTENTS</div>
    <p class="body-copy" style="top:42px;">&nbsp;ALIGNER&nbsp; GEL&nbsp; is&nbsp; a proprietary<br>blend of natural plant extract<br>including Angelica, Radix Rehmanniae<br>Coptis, Honeysuckle, Echinacea, Sage<br>Chamomile&nbsp; and&nbsp; Acerola cherry</p>

    <div class="section-head" style="top:150px;">DIRECTIONS OF USE</div>
    <p class="body-copy" style="top:170px;">Drop on the teeth directly after<br>&nbsp;brushing Or put into clear aligners<br>before wearing again. No need to<br>&nbsp;to rinse your mouth with water</p>

    <div class="spine-text">30ML / 1 FL OZ</div>

    <div class="wordmark" style="left:446px;width:236px;top:40px;font-size:28px;">Lumi Leaf<span class="dot" style="width:9px;height:9px;"></span></div>
    <div class="abs" style="left:446px;width:236px;top:110px;font-size:23px;font-weight:600;letter-spacing:0.5px;">ALIGNER GEL</div>
    <div class="abs caps" style="left:446px;width:236px;top:146px;font-size:11.5px;line-height:18px;letter-spacing:1.4px;">Immune support for<br>oral health</div>
    <div class="abs" style="left:446px;width:236px;top:190px;font-size:12px;line-height:17px;font-weight:600;">The Solution to Maintain Dental<br>Hygiene and Strengthen Gums</div>
    <div class="abs" style="left:446px;width:236px;top:237px;font-size:8.5px;letter-spacing:1.2px;">MADE IN TAIWAN</div>
  </section>

</main>
</body>
</html>
```